Magazine advertisement

I need a company advertisement for magazine prints. I need to be able to scale it to different sizes if need be. I need it to showcase our brand, VornaDrive have our phone number 582.463.9047 our contact email address sales@vornadrive.net and web address www.vornadrive.net

Target Market(s)

automotive / tractor pulling

Industry/Entity Type

automotive / racing

Colors
EB3D1F
EC4F4E
F09395
F8D3D4
FCEDEE

Requirements
Must have
• our logo, our color scheme (pantone red 1795, white, black, silver

```html
<!DOCTYPE html>
<html lang="en">
<head>
<meta charset="utf-8">
<title>VornaDrive – Custom Turbochargers</title>
<link href="https://fonts.googleapis.com/css2?family=Fira+Sans:wght@300;400;700;800&family=PT+Sans:wght@400;700&display=swap" rel="stylesheet">
<style>
  :root {
    --red: #d0202a;
    --red-bright: #ed1c24;
    --red-deep: #a3161d;
    --black: #0c0c0c;
    --silver: #c9cbcd;
    --steel: #8e9296;
    --slate-a: #7d98a6;
    --slate-b: #5d6b75;
    --white: #ffffff;
    --ink: #1a1a1a;
  }
  * { margin: 0; padding: 0; box-sizing: border-box; }
  html, body { width: 1040px; height: 1200px; overflow: hidden; background: #ffffff; }
  .ad {
    position: relative; width: 1040px; height: 1200px; overflow: hidden;
    background: linear-gradient(180deg, #dfe9f2 0%, #ffffff 22%, #ffffff 100%);
    font-family: "PT Sans", sans-serif;
  }
  .brand {
    position: absolute; left: 79px; top: 210px;
    font-family: "Fira Sans", sans-serif; font-weight: 800; font-size: 66px;
    color: var(--red-bright); letter-spacing: 1px;
  }
  .shapes { position: absolute; left: 0; top: 0; }
  .hero-photo {
    position: absolute; left: 497px; top: 78px; width: 488px; height: 460px;
    border-radius: 48% 46% 44% 50%;
    background: radial-gradient(circle at 42% 52%, #f4f5f6 0%, #c8cacc 45%, #7f8386 80%, #55585b 100%);
  }
  .headline {
    position: absolute; left: 79px; top: 440px; color: var(--white);
    font-family: "Fira Sans", sans-serif;
  }
  .headline h1 { font-weight: 800; font-size: 42px; line-height: 42px; letter-spacing: 0.3px; }
  .headline p { font-weight: 300; font-size: 30px; margin-top: 8px; letter-spacing: 0.2px; }
  .headline .rule { width: 62px; height: 5px; background: var(--white); margin-top: 14px; }
  .callout {
    position: absolute; left: 752px; top: 548px; width: 280px;
    color: var(--white); font-family: "Fira Sans", sans-serif; font-size: 20px; line-height: 26px; text-align: center;
  }
  .callout strong { font-weight: 700; }
  .info {
    position: absolute; left: 0; top: 623px; width: 1040px; height: 239px;
    background: linear-gradient(100deg, #1b1b1b 0%, #0a0a0a 45%, #151515 70%, #000 100%);
  }
  .info-col { position: absolute; top: 32px; width: 190px; color: var(--white); }
  .info-col h2 { font-family: "Fira Sans", sans-serif; font-weight: 700; font-size: 28px; margin-bottom: 12px; white-space: nowrap; }
  .info-col p { font-size: 11.5px; line-height: 16px; }
  .info-col.what { left: 91px; } .info-col.what p { text-align: justify; }
  .info-col.history { left: 432px; }
  .info-col.product { left: 767px; } .info-col.product p { text-align: justify; }
  .divider { position: absolute; top: 36px; width: 1px; height: 170px; background: #5a5a5a; }
  .gallery { position: absolute; left: 158px; top: 844px; height: 127px; display: flex; }
  .gallery div { height: 100%; }
  .photo-desert { width: 198px; background: linear-gradient(170deg, #8a9bb0 0%, #9d7a55 40%, #b07a45 100%); }
  .photo-drag { width: 294px; background: linear-gradient(180deg, #c9ccd0 0%, #e2e4e6 50%, #b83a40 78%, #8d8f92 100%); }
  .photo-tractor { width: 230px; background: linear-gradient(180deg, #5e6b78 0%, #4a4f55 45%, #a8343a 70%, #8b7a63 100%); }
  .cta {
    position: absolute; left: 409px; top: 960px; width: 231px; height: 66px;
    border-radius: 18px; background: linear-gradient(180deg, var(--red) 0%, var(--red-deep) 100%);
    color: var(--white); font-family: "Fira Sans", sans-serif; font-weight: 700; font-size: 28px;
    display: flex; align-items: center; justify-content: center;
  }
  .cta-copy {
    position: absolute; left: 335px; top: 1041px; width: 390px;
    font-size: 10.5px; line-height: 14px; text-align: center; color: var(--ink);
  }
  .footer {
    position: absolute; left: 0; top: 1125px; width: 1040px; height: 75px;
    background: linear-gradient(90deg, var(--slate-b) 0%, var(--slate-a) 50%, var(--slate-b) 100%);
    color: var(--white); font-family: "Fira Sans", sans-serif;
  }
  .footer-web {
    position: absolute; left: 0; right: 0; top: 0; height: 75px;
    display: flex; align-items: center; justify-content: center;
    font-weight: 400; font-size: 20px; letter-spacing: 13px; padding-left: 13px;
  }
  .footer-contact {
    position: absolute; top: 0; height: 75px; display: flex; align-items: center;
    font-weight: 400; font-size: 15px; letter-spacing: 1px;
  }
  .footer-contact.phone { left: 60px; }
  .footer-contact.email { right: 60px; }
</style>
</head>
<body>
<div class="ad">
  <svg class="shapes" width="1040" height="1200" viewBox="0 0 1040 1200" aria-hidden="true">
    <defs>
      <linearGradient id="bandRed" x1="0" x2="1" y1="0" y2="0">
        <stop offset="0" stop-color="#a3161d"/>
        <stop offset="1" stop-color="#e0232b"/>
      </linearGradient>
    </defs>
    <path class="red-band" d="M0 368 H770 L700 606 Q694 623 672 623 H0 Z" fill="url(#bandRed)"/>
    <rect class="steel-strip" x="760" y="498" width="280" height="26" fill="#8e9296"/>
    <path class="callout-box" d="M742 524 H1040 V649 H770 L706 586 Z" fill="#ed1c24"/>
  </svg>

  <div class="brand">VornaDrive</div>

  <div class="hero-photo" role="img" aria-label="Polished silver billet turbocharger with exposed compressor wheel"></div>

  <div class="headline">
    <h1>CUSTOM<br>TURBOCHARGERS</h1>
    <p>FOR EXTREME MOTORSPORTS</p>
    <div class="rule"></div>
  </div>

  <div class="callout"><strong>Excellence</strong> in Custom Truck Modification and Upfitting</div>

  <section class="info">
    <div class="info-col what">
      <h2>What We Do?</h2>
      <p>We’ll help you perform like a winner, from truck and tractor pulling to drag racing. Our turbochargers are equipped with the capacity to power everything from high-end sports cars to snowmobiles.</p>
    </div>
    <div class="divider" style="left:342px"></div>
    <div class="info-col history">
      <h2>Our History</h2>
      <p>In 2019, we took the racing world by storm after unveiling our revolutionary turbocharger at the Grand Horsepower Trade Expo. During this event, our company set a new standard for turbocharged engines.</p>
    </div>
    <div class="divider" style="left:692px"></div>
    <div class="info-col product">
      <h2>Our Product</h2>
      <p>Our team utilizes groundbreaking techniques to create upscale turbochargers that are guaranteed to defy your expectations. Our unique, patented wheel-design and advanced technology optimizes performance for a wide range of specialized vehicles.</p>
    </div>
  </section>

  <div class="gallery">
    <div class="photo-desert" role="img" aria-label="Off-road truck kicking up dust on a desert track"></div>
    <div class="photo-drag" role="img" aria-label="Drag racing car launching down the strip"></div>
    <div class="photo-tractor" role="img" aria-label="Red pulling tractor in an indoor arena"></div>
  </div>

  <div class="cta">Built to Win</div>

  <p class="cta-copy">We’ll help you perform like a winner, from truck and tractor pulling to drag racing. Our turbochargers are equipped with the capacity to power everything from high-end sports cars to snowmobiles.</p>

  <footer class="footer">
    <span class="footer-contact phone">582.463.9047</span>
    <span class="footer-web">www.vornadrive.net</span>
    <span class="footer-contact email">sales@vornadrive.net</span>
  </footer>
</div>
</body>
</html>
```